TALBRIDGE ELEVATOR CORP

LOOKING FOR BLACK MATTE BACKGROUND WITH GLOSS DESIGN
NEED RAISED UV ON LOGO AND LETTERING , WITH ROUNDED CORNERS AND COLORED EDGES ( FLOURECENT BLUE)

```html
<!DOCTYPE html>
<html lang="en">
<head>
<meta charset="utf-8">
<title>Talbridge Elevator Corp – Business Cards</title>
<link rel="stylesheet" href="https://fonts.googleapis.com/css2?family=Montserrat:wght@400;500;700&display=swap">
<style>
  :root {
    --backdrop: #5a5a5a;
    --card-black: #2b2b2c;
    --edge-blue: #12a6e6;
    --gloss-silver: #c4c4c4;
    --gloss-bright: #e2e2e2;
    --mark-blue: #2f86c9;
  }
  * { box-sizing: border-box; margin: 0; padding: 0; }
  html, body {
    width: 1200px; height: 1021px; overflow: hidden;
    background: var(--backdrop);
    font-family: "Montserrat", sans-serif;
  }
  .stage {
    position: relative; width: 1200px; height: 1021px;
  }
  .card {
    position: absolute; left: 300px;
    width: 600px; height: 343px;
    background: var(--card-black);
    border-radius: 30px;
    box-shadow: 0 7px 0 var(--edge-blue), 0 18px 30px rgba(0,0,0,0.35);
    color: var(--gloss-silver);
  }
  .card--front { top: 120px; }
  .card--back { top: 560px; }

  /* front */
  .front-mark {
    position: absolute; left: 0; right: 0; top: 92px;
    display: flex; align-items: center; justify-content: center; gap: 16px;
  }
  .mark-dot {
    width: 46px; height: 46px; border-radius: 50%;
    background: var(--mark-blue);
  }
  .mark-name {
    font-weight: 700; font-size: 26px; letter-spacing: 2px;
    color: var(--gloss-silver);
  }
  .front-title {
    position: absolute; left: 0; right: 0; top: 196px;
    text-align: center;
    font-weight: 700; font-size: 25px; letter-spacing: 1px;
    color: var(--gloss-bright);
  }
  .front-tagline {
    position: absolute; left: 0; right: 0; top: 234px;
    text-align: center;
    font-weight: 400; font-size: 15px; letter-spacing: 2px;
  }

  /* back */
  .back-mark {
    position: absolute; left: 48px; top: 82px;
    display: flex; align-items: center; gap: 12px;
  }
  .back-mark .mark-dot { width: 40px; height: 40px; }
  .back-mark .mark-name { font-size: 20px; }
  .contact {
    position: absolute; left: 315px; top: 66px;
    font-size: 15px; line-height: 1.35;
  }
  .contact-name {
    font-weight: 500; font-size: 22px; letter-spacing: 1px;
    color: var(--gloss-bright);
  }
  .contact-role { font-size: 15px; margin-bottom: 14px; }
  .contact-address { margin-bottom: 6px; }
  .contact-line { display: flex; align-items: center; gap: 8px; font-size: 14px; }
  .contact-line svg { width: 14px; height: 14px; flex: none; }
  .established {
    position: absolute; left: 0; width: 300px; top: 290px;
    text-align: center; font-size: 16px; letter-spacing: 1px;
  }
</style>
</head>
<body>
<main class="stage">
  <section class="card card--front">
    <div class="front-mark">
      <span class="mark-dot"></span>
      <span class="mark-name">TALBRIDGE</span>
    </div>
    <h1 class="front-title">TALBRIDGE ELEVATOR CORP</h1>
    <p class="front-tagline">ELEVATOR SERVICES</p>
  </section>

  <section class="card card--back">
    <div class="back-mark">
      <span class="mark-dot"></span>
      <span class="mark-name">TALBRIDGE</span>
    </div>
    <div class="contact">
      <h2 class="contact-name">DANIEL MARSH</h2>
      <p class="contact-role">President</p>
      <p class="contact-address">2241 Harlow Ave,<br>Bronx 10465</p>
      <p class="contact-line">
        <svg viewBox="0 0 14 14" fill="none" stroke="currentColor" stroke-width="1.3"><rect x="3.5" y="1" width="7" height="12" rx="1.2"/></svg>
        516-555-0147
      </p>
      <p class="contact-line">
        <svg viewBox="0 0 14 14" fill="none" stroke="currentColor" stroke-width="1.3"><rect x="1" y="3" width="12" height="8"/><path d="M1 3l6 5 6-5"/></svg>
        talbridgeelevator@mail.com
      </p>
      <p class="contact-line">
        <svg viewBox="0 0 14 14" fill="none" stroke="currentColor" stroke-width="1.2"><circle cx="7" cy="7" r="6"/><ellipse cx="7" cy="7" rx="2.6" ry="6"/><path d="M1 7h12"/></svg>
        www.talbridgeelevatorny.com
      </p>
    </div>
    <p class="established">ESTABLISHED 1978</p>
  </section>
</main>
</body>
</html>
```